Business Card Design- Mortgage Firm

Looking to design a business Card for our Outside sales people. This card is used to provide their contact information to prospective clients and realtors. Must have All Pertinent company and licensing information by law. We are looking for a very modern design that flows with our current logo color scheme. Red/White/Black

Industry/Entity Type

Mortgage Lender

Contact Information for Business Card

Must stick with current color scheme.

Colors
f04a50
ffffff
ecf7fb

Requirements
Must have
• Company Logo or similar
• Company Address (748 W Alder Avenue, Suite 312, Corona CA 92879 NMLS: 4072916)
• Agent Name (Mira Talbot)
• Title (Senior Mortgage Loan Originator)
• NMLS# 8395021
• Toll Free: 800-627-3184
• Direct : 310-555-4860
Nice to have
• Room for Agent Picture

```html
<!DOCTYPE html>
<html lang="en">
<head>
<meta charset="utf-8">
<title>Redwell Mortgage – Business Card</title>
<link rel="stylesheet" href="https://fonts.googleapis.com/css2?family=Open+Sans:wght@400;600;700&display=swap">
<style>
  :root {
    --brand-red: #b5202a;
    --band-red: #b3212b;
    --ink: #3a3a3a;
    --ink-dark: #111111;
    --rule: #6b6b6b;
    --card: #ffffff;
    --tag-grey: #e6e7e9;
    --backdrop: #2e241f;
    --photo-light: #d9cfc6;
    --photo-dark: #6b5647;
  }
  * { margin: 0; padding: 0; box-sizing: border-box; }
  html, body {
    width: 1200px; height: 801px; overflow: hidden;
    background: var(--backdrop);
    font-family: "Open Sans", Arial, sans-serif;
  }
  .stage { position: relative; width: 1200px; height: 801px; }
  .card {
    position: absolute; left: 150px; top: 141px;
    width: 890px; height: 507px;
    background: var(--card); overflow: hidden;
  }
  .brand {
    position: absolute; left: 75px; top: 52px;
    display: flex; align-items: center; gap: 24px;
  }
  .brand-mark { width: 96px; height: 96px; background: var(--brand-red); flex: none; }
  .brand-name {
    color: var(--brand-red); font-weight: 700;
    font-size: 44px; letter-spacing: 2px; text-transform: uppercase; line-height: 1.08;
  }
  .agent-photo {
    position: absolute; left: 560px; top: 34px; width: 330px; height: 473px;
    background: radial-gradient(ellipse at 55% 35%, var(--photo-light) 0%, #b89a80 45%, var(--photo-dark) 100%);
    border-radius: 150px 150px 0 0;
  }
  .contact {
    position: absolute; left: 118px; top: 237px; width: 343px;
    text-align: center; font-size: 20px; line-height: 1;
  }
  .contact .toll { color: var(--brand-red); font-weight: 700; margin-bottom: 15px; }
  .contact .direct { color: var(--brand-red); font-weight: 400; }
  .contact .rule { height: 2px; background: var(--rule); margin: 19px 0 19px; }
  .contact .address { color: var(--ink); font-size: 20px; line-height: 31px; }
  .name-band {
    position: absolute; left: 0; top: 414px; width: 612px; height: 52px;
    background: var(--band-red);
    clip-path: polygon(0 0, 100% 0, 94% 100%, 0 100%);
    color: #fff; display: flex; align-items: baseline; padding: 7px 0 0 38px;
  }
  .name-band .agent-name { font-size: 28px; font-weight: 700; }
  .name-band .agent-title { font-size: 17px; font-weight: 400; margin-left: 8px; text-transform: uppercase; }
  .license-tag {
    position: absolute; left: 545px; top: 442px; width: 345px; height: 42px;
    background: var(--tag-grey);
    clip-path: polygon(12% 0, 100% 0, 100% 100%, 0 100%);
    color: var(--ink-dark); font-weight: 700; font-size: 20px;
    padding: 8px 0 0 117px;
  }
</style>
</head>
<body>
<div class="stage">
  <div class="card">
    <div class="agent-photo" role="img" aria-label="Portrait photo of the loan originator"></div>

    <div class="brand">
      <div class="brand-mark"></div>
      <div class="brand-name">Redwell<br>Mortgage</div>
    </div>

    <div class="contact">
      <p class="toll">Toll Free: 800-627-3184</p>
      <p class="direct">Direct : 310-555-4860</p>
      <div class="rule"></div>
      <p class="address">748 W Alder Avenue, Suite 312,<br>Corona CA 92879 NMLS: 4072916</p>
    </div>

    <div class="name-band">
      <span class="agent-name">Mira Talbot,</span>
      <span class="agent-title">Senior Mortgage Loan Originator</span>
    </div>

    <div class="license-tag">NMLS# 8395021</div>
  </div>
</div>
</body>
</html>
```